Talvero Engineering & Management Services Website

A professional website design that outlines Engineering and Management Services. The website is to be colour coordinated with the current logo (see attached). The webpage needs to be compatible with Wordpress to allow for easy changes to be made to the website for the user.
Required tabs for the page include:
- Civil Engineering
- Structural Engineering
- Project Management
- Business Management
- Project Controls
- Drafting
- Contact Us

Clean and efficient website that matches the services provided by the business.

Target Market(s)

New Customers to a very competitive market

Industry/Entity Type

Engineering

Number of Pages Required

5+ page

Requirements
Must have
• Clean with large stock photos

```html
<!DOCTYPE html>
<html lang="en">
<head>
<meta charset="utf-8">
<title>Talvero Engineering &amp; Management Services</title>
<link href="https://fonts.googleapis.com/css2?family=Oswald:wght@400;500;600&family=Roboto:wght@400;500;700&display=swap" rel="stylesheet">
<style>
:root{
  --orange:#f26b21;
  --orange-dark:#d95a14;
  --ink:#333;
  --muted:#777;
  --nav:#4a4a4a;
  --light:#f2f2f2;
  --footer:#2b2b2b;
  --footer-bar:#1f1f1f;
  --green:#7cb82f;
  --white:#fff;
}
*{box-sizing:border-box;margin:0;padding:0}
html,body{width:683px;height:1200px;overflow:hidden}
body{font-family:"Roboto",Arial,sans-serif;color:var(--ink);background:var(--white);font-size:7px;line-height:1.5}
.site-header{height:66px;display:flex;align-items:center;justify-content:space-between;padding:0 22px}
.brand{display:flex;align-items:center;gap:8px}
.brand-dot{width:40px;height:40px;border-radius:50%;background:var(--orange)}
.brand-name{font-family:"Oswald",sans-serif;font-weight:600;color:var(--ink);font-size:12px;line-height:1.15;letter-spacing:.5px;text-transform:uppercase}
.header-right{display:flex;align-items:center;gap:14px}
.social{display:flex;gap:5px}
.social span{width:16px;height:16px;border-radius:50%;background:#bdbdbd;display:block}
.call{text-align:right}
.call small{display:block;font-size:7.5px;color:var(--ink);font-weight:500}
.call strong{font-family:"Oswald",sans-serif;color:var(--orange);font-size:13px;font-weight:500}
.main-nav{height:24px;background:var(--nav);display:flex;padding:0 12px}
.main-nav a{color:#eee;text-decoration:none;font-size:6.6px;font-weight:500;letter-spacing:.3px;padding:0 9px;display:flex;align-items:center;text-transform:uppercase}
.main-nav a.active{background:var(--orange);color:var(--white)}
.hero{position:relative;height:300px;background:linear-gradient(100deg,#eef0f1 0%,#dfe3e6 35%,#b9aea3 55%,#e36b2a 68%,#8f9296 85%,#5d6066 100%)}
.hero-copy{position:absolute;left:22px;top:36px;width:190px}
.hero-copy h1{font-family:"Oswald",sans-serif;font-size:27px;line-height:1.1;font-weight:600;color:#222;text-transform:uppercase}
.hero-copy p{font-size:9px;color:#333;margin:8px 0 12px}
.btn-outline{display:inline-block;border:1.5px solid #222;padding:4px 9px;font-size:8px;font-weight:700;color:#222;text-transform:uppercase;background:rgba(255,255,255,.6)}
.slider-dots{position:absolute;bottom:8px;left:50%;transform:translateX(-50%);display:flex;gap:4px}
.slider-dots span{width:6px;height:6px;border-radius:50%;background:#fff;opacity:.7}
.slider-dots span.on{background:var(--orange);opacity:1}
.services{display:flex;gap:4px;padding:6px 6px;background:#e9e9e9;height:112px}
.service{flex:1;display:flex;flex-direction:column}
.service-photo{height:56px;background:linear-gradient(160deg,#c7d3dc,#8fa3b3)}
.service:nth-child(2) .service-photo{background:linear-gradient(160deg,#d9dde0,#7f8c96)}
.service:nth-child(3) .service-photo{background:linear-gradient(160deg,#e8d8c8,#a7886c)}
.service:nth-child(4) .service-photo{background:linear-gradient(160deg,#d0d6de,#6f7b89)}
.service:nth-child(5) .service-photo{background:linear-gradient(160deg,#c6dff0,#5b8cb0)}
.service:nth-child(6) .service-photo{background:linear-gradient(160deg,#e4e6e8,#9ea5ab)}
.service-label{flex:1;background:var(--orange);color:var(--white);font-size:8px;font-weight:500;padding:5px 6px;line-height:1.2}
.welcome{display:flex;gap:24px;padding:34px 22px 30px;height:244px}
.welcome-text{flex:1}
.section-title{font-family:"Oswald",sans-serif;color:var(--orange);font-size:11px;font-weight:500;text-transform:uppercase;letter-spacing:.3px;margin-bottom:8px}
.welcome-text p{color:var(--muted);margin-bottom:10px}
.feature{width:198px}
.feature-photo{height:96px;background:linear-gradient(135deg,#6b4a37,#c48b5b 50%,#3d2d25)}
.feature-row{display:flex;justify-content:space-between;align-items:center;margin-top:6px}
.feature-row strong{font-size:9px;line-height:1.2;width:110px}
.btn-green{background:var(--green);color:var(--white);font-size:6px;font-weight:700;padding:4px 10px;text-transform:uppercase}
.testimonials{background:var(--light);padding:20px 22px 26px;text-align:center;height:262px}
.testimonials .intro{color:var(--muted);width:470px;margin:0 auto 18px}
.quotes{display:flex;gap:26px;text-align:left}
.quote{flex:1}
.quote-mark{font-family:"Oswald",sans-serif;color:#c9c9c9;font-size:22px;line-height:1;text-align:center}
.quote p{color:var(--muted);text-align:center;margin:4px 0 12px}
.quote-by{display:flex;align-items:center;gap:6px;justify-content:space-between;font-weight:700;font-size:8px}
.avatar{width:22px;height:22px;border-radius:50%;background:linear-gradient(135deg,#f58a4c,#c9531b)}
.site-footer{background:var(--footer);color:#bbb;position:relative;height:218px;padding:44px 22px 0}
.footer-dot{position:absolute;left:50%;top:-16px;transform:translateX(-50%);width:34px;height:34px;border-radius:50%;background:var(--orange);border:3px solid var(--footer)}
.footer-cols{display:flex;gap:24px}
.footer-col{flex:1}
.footer-col h4{color:var(--white);font-size:8px;font-weight:700;text-transform:uppercase;margin-bottom:8px}
.news-item{display:flex;gap:6px;margin-bottom:10px}
.news-thumb{width:22px;height:20px;background:#555;flex:none}
.news-item span{font-size:6.5px;line-height:1.4}
.contact-line{display:flex;gap:6px;margin-bottom:7px;font-size:6.5px}
.contact-line svg{flex:none}
.footer-col ul{list-style:none}
.footer-col li{font-size:6.5px;margin-bottom:3px}
.footer-bar{position:absolute;left:0;right:0;bottom:0;height:22px;background:var(--footer-bar);display:flex;align-items:center;justify-content:space-between;padding:0 22px;font-size:6px;color:#888}
.footer-bar .social span{width:11px;height:11px;background:#555}
</style>
</head>
<body>
<header class="site-header">
  <div class="brand">
    <span class="brand-dot"></span>
    <div class="brand-name">Talvero<br>Engineering &amp; Management Services</div>
  </div>
  <div class="header-right">
    <div class="social"><span></span><span></span><span></span></div>
    <div class="call"><small>Questions? Call Us</small><strong>1-800-555-0142</strong></div>
  </div>
</header>
<nav class="main-nav">
  <a class="active" href="#">Home</a><a href="#">Civil Engineering</a><a href="#">Structural Engineering</a><a href="#">Project Management</a><a href="#">Business Management</a><a href="#">Project Controls</a><a href="#">Drafting</a><a href="#">Contact Us</a>
</nav>
<section class="hero" role="img" aria-label="Engineers in hard hats and safety vests reviewing plans on a laptop at a construction site">
  <div class="hero-copy">
    <h1>Lorem Ipsum Dolor Sit Amet</h1>
    <p>Sed ut perspiciatis unde omnis iste natus error sit voluptatem accusantium</p>
    <span class="btn-outline">Learn More</span>
  </div>
  <div class="slider-dots"><span class="on"></span><span></span><span></span><span></span><span></span></div>
</section>
<section class="services">
  <div class="service"><div class="service-photo" role="img" aria-label="Civil engineering site photo"></div><div class="service-label">Civil<br>Engineering</div></div>
  <div class="service"><div class="service-photo" role="img" aria-label="Structural steel frame photo"></div><div class="service-label">Structural<br>Engineering</div></div>
  <div class="service"><div class="service-photo" role="img" aria-label="Project team meeting photo"></div><div class="service-label">Project<br>Management</div></div>
  <div class="service"><div class="service-photo" role="img" aria-label="Business meeting photo"></div><div class="service-label">Business<br>Management</div></div>
  <div class="service"><div class="service-photo" role="img" aria-label="Project control charts photo"></div><div class="service-label">Project<br>Controls</div></div>
  <div class="service"><div class="service-photo" role="img" aria-label="Technical drafting photo"></div><div class="service-label">Drafting</div></div>
</section>
<section class="welcome">
  <div class="welcome-text">
    <h2 class="section-title">Welcome to Talvero Engineering and Management Services</h2>
    <p>Lorem ipsum dolor sit amet, consectetur adipiscing elit, sed do eiusmod tempor incididunt ut labore et dolore magna aliqua. Ut enim ad minim veniam, quis nostrud exercitation ullamco laboris nisi ut aliquip ex ea commodo consequat. Duis aute irure dolor in reprehenderit in voluptate velit esse cillum dolore eu fugiat nulla pariatur. Excepteur sint occaecat cupidatat non proident, sunt in culpa qui officia deserunt mollit anim id est laborum.</p>
    <p>Duis aute irure dolor in reprehenderit in voluptate velit esse cillum dolore eu fugiat nulla pariatur. Excepteur sint occaecat cupidatat non proident, sunt in culpa qui officia deserunt mollit anim id est laborum.</p>
  </div>
  <aside class="feature">
    <div class="feature-photo" role="img" aria-label="Team gathered around a table in discussion"></div>
    <div class="feature-row"><strong>Lorem ipsum dolor sit amet</strong><span class="btn-green">Watch Now</span></div>
  </aside>
</section>
<section class="testimonials">
  <h2 class="section-title">What Our People Are Saying</h2>
  <p class="intro">Lorem ipsum dolor sit amet, consectetur adipiscing elit, sed do eiusmod tempor incididunt ut labore et dolore magna aliqua. Ut enim ad minim veniam.</p>
  <div class="quotes">
    <div class="quote"><div class="quote-mark">&ldquo;</div><p>Sed ut perspiciatis unde omnis iste natus error sit voluptatem accusantium doloremque laudantium, totam rem aperiam, eaque ipsa quae ab illo inventore veritatis et quasi architecto beatae vitae dicta sunt explicabo. Nemo enim ipsam voluptatem quia voluptas sit.</p><div class="quote-by"><span>Daniel</span><span class="avatar" role="img" aria-label="Client portrait"></span></div></div>
    <div class="quote"><div class="quote-mark">&ldquo;</div><p>Sed ut perspiciatis unde omnis iste natus error sit voluptatem accusantium doloremque laudantium, totam rem aperiam, eaque ipsa quae ab illo inventore veritatis et quasi architecto beatae vitae dicta sunt explicabo. Nemo enim ipsam voluptatem quia voluptas sit.</p><div class="quote-by"><span>Daniel</span><span class="avatar" role="img" aria-label="Client portrait"></span></div></div>
    <div class="quote"><div class="quote-mark">&ldquo;</div><p>Sed ut perspiciatis unde omnis iste natus error sit voluptatem accusantium doloremque laudantium, totam rem aperiam, eaque ipsa quae ab illo inventore veritatis et quasi architecto beatae vitae dicta sunt explicabo. Nemo enim ipsam voluptatem quia voluptas sit.</p><div class="quote-by"><span>Daniel</span><span class="avatar" role="img" aria-label="Client portrait"></span></div></div>
  </div>
</section>
<footer class="site-footer">
  <span class="footer-dot"></span>
  <div class="footer-cols">
    <div class="footer-col"><h4>Recent News</h4>
      <div class="news-item"><span class="news-thumb"></span><span>Nunc sed risus quam Morbi gravida quam nisi</span></div>
      <div class="news-item"><span class="news-thumb"></span><span>Nunc sed risus quam Morbi gravida quam nisi</span></div>
    </div>
    <div class="footer-col"><h4>Recent Blog</h4>
      <div class="news-item"><span class="news-thumb"></span><span>Nunc sed risus quam Morbi gravida quam nisi</span></div>
      <div class="news-item"><span class="news-thumb"></span><span>Nunc sed risus quam Morbi gravida quam nisi</span></div>
    </div>
    <div class="footer-col"><h4>Contact Us</h4>
      <div class="contact-line"><svg width="8" height="10" viewBox="0 0 8 10"><path d="M4 0a4 4 0 0 0-4 4c0 3 4 6 4 6s4-3 4-6a4 4 0 0 0-4-4zm0 5.5A1.5 1.5 0 1 1 4 2.5a1.5 1.5 0 0 1 0 3z" fill="#f26b21"/></svg><span>214 Harbor Ridge Road, Suite 300<br>Fairview, ON 00000</span></div>
      <div class="contact-line"><svg width="8" height="8" viewBox="0 0 8 8"><path d="M1.6 0 3 1.8 2.2 3a5 5 0 0 0 2.8 2.8L6.2 5 8 6.4 7 8C3 8 0 5 0 1z" fill="#f26b21"/></svg><span>1-800-555-0142</span></div>
      <div class="contact-line"><svg width="9" height="7" viewBox="0 0 9 7"><rect width="9" height="7" rx="1" fill="#f26b21"/><path d="M.5.8 4.5 4 8.5.8" stroke="#2b2b2b" fill="none"/></svg><span>info@talvero-ems.com</span></div>
    </div>
    <div class="footer-col"><h4>Quick Links</h4>
      <ul><li>Civil Engineering</li><li>Structural Engineering</li><li>Project Management</li><li>Business Management</li><li>Project Controls</li><li>Drafting</li></ul>
    </div>
  </div>
  <div class="footer-bar">
    <span>&copy; 2015 Talvero. All Rights Reserved &middot; Terms and Conditions &middot; Privacy Policy &middot; Terms of Use</span>
    <div class="social"><span></span><span></span><span></span></div>
  </div>
</footer>
</body>
</html>
```